Stationery for Software Developer
Glen Ambrose
Project: Stationery for Software Developer
Stationery for Software Developer - Information Technology
Creative Brief
Professional
Software Engineer
Greater Seattle Area
glen@ambrosk.me
http://ambrosk.me
Chirpline: @ambrog Circlr+: +GlenAmbrose Facepage: gambrosk WorkNexus: glenambrose (Prefer Social Icons to be used instead of the names)
Main Logo with name on front. Open to variations of the main logo on front.
sevensky sevensky
gambrosk gambrosk
My apologies. I accidentally started this project before I had my logo in hand. I have contacted support about suspending this contest for 4 days until I have it. Thanks for the interest! Glen
paul1990 paul1990
Hi, Where is your logo?

```html
<!DOCTYPE html>
<html lang="en">
<head>
<meta charset="utf-8">
<title>Glen Ambrose – Business Cards</title>
<link href="https://fonts.googleapis.com/css2?family=Raleway:wght@300;400;500&display=swap" rel="stylesheet">
<style>
  :root {
    --page-bg: #e9e9ea;
    --card-white: #ffffff;
    --ink-grey: #5a5d66;
    --slate: #3f4a63;
    --slate-light: #d6dbe6;
    --pink: #e2428f;
    --pink-soft: #f4b6d3;
    --teal: #7fd0c6;
    --purple: #9b7fc4;
    --back-blue: #d3ecf6;
    --back-pink: #f6dbea;
  }
  * { box-sizing: border-box; margin: 0; padding: 0; }
  html, body {
    width: 1200px; height: 600px; overflow: hidden;
    background: var(--page-bg);
    font-family: "Raleway", "Helvetica Neue", Arial, sans-serif;
  }
  .canvas { position: relative; width: 1200px; height: 600px; }

  .card {
    position: absolute; top: 145px;
    width: 540px; height: 310px;
    overflow: hidden;
    box-shadow: 0 6px 18px rgba(0,0,0,0.18);
  }

  /* Front */
  .card-front { left: 40px; background: var(--card-white); }
  .front-mark {
    position: absolute; left: 38px; top: 48px;
    width: 44px; height: 44px;
    background: var(--purple);
  }
  .front-divider {
    position: absolute; left: 96px; top: 46px;
    width: 1px; height: 48px; background: #c9cbd1;
  }
  .front-name {
    position: absolute; left: 108px; top: 50px;
    font-size: 36px; font-weight: 300; color: var(--ink-grey);
    letter-spacing: 0.5px;
  }
  .front-band { position: absolute; left: 0; top: 0; }
  .band-identity {
    position: absolute; left: 38px; top: 190px; color: #fff;
  }
  .band-identity .person { font-size: 17px; font-weight: 400; }
  .band-identity .role { font-size: 10px; font-weight: 300; margin-top: 2px; color: var(--slate-light); }
  .band-contact {
    position: absolute; left: 235px; top: 160px; color: #fff;
  }
  .band-contact .region { font-size: 13px; font-weight: 400; margin-bottom: 8px; }
  .contact-line {
    display: flex; align-items: center; gap: 6px;
    font-size: 10.5px; font-weight: 300; margin-top: 4px;
  }
  .contact-line svg { width: 10px; height: 10px; fill: #fff; }
  .front-web {
    position: absolute; left: 0; right: 0; bottom: 22px; padding-left: 180px;
    font-size: 15px; font-weight: 400; color: var(--pink); letter-spacing: 0.5px;
  }

  /* Back */
  .card-back {
    left: 620px;
    background: linear-gradient(125deg, var(--back-blue) 0%, #f7fbfd 38%, var(--back-pink) 62%, #eef5fb 100%);
  }
  .back-name {
    position: absolute; left: 0; right: 0; top: 92px; text-align: center;
    font-size: 40px; font-weight: 300; color: var(--ink-grey);
  }
  .social-list {
    position: absolute; left: 30px; right: 30px; top: 166px;
    display: flex; flex-wrap: wrap; justify-content: center; gap: 8px 18px;
    list-style: none;
  }
  .social-item {
    display: flex; align-items: center; gap: 5px;
    font-size: 11px; font-weight: 400; color: var(--ink-grey);
  }
  .social-dot { width: 9px; height: 9px; border-radius: 50%; background: var(--slate); }
  .back-web {
    position: absolute; left: 0; right: 0; bottom: 48px; text-align: center;
    font-size: 16px; font-weight: 400; color: var(--pink); letter-spacing: 1px;
  }
</style>
</head>
<body>
<main class="canvas">

  <section class="card card-front" aria-label="Business card front">
    <div class="front-mark"></div>
    <div class="front-divider"></div>
    <h1 class="front-name">Glen Ambrose</h1>

    <svg class="front-band" width="540" height="310" viewBox="0 0 540 310" aria-hidden="true">
      <polygon points="0,142 470,118 466,130 0,152" fill="var(--pink)"/>
      <polygon points="0,152 466,130 430,250 0,250" fill="var(--slate)"/>
    </svg>

    <div class="band-identity">
      <div class="person">Glen Ambrose</div>
      <div class="role">Software Engineer</div>
    </div>

    <div class="band-contact">
      <div class="region">Greater Seattle Area</div>
      <div class="contact-line">
        <svg viewBox="0 0 10 10" aria-hidden="true"><path d="M5 0a3.4 3.4 0 0 0-3.4 3.4C1.6 6 5 10 5 10s3.4-4 3.4-6.6A3.4 3.4 0 0 0 5 0zm0 4.8a1.4 1.4 0 1 1 0-2.8 1.4 1.4 0 0 1 0 2.8z"/></svg>
        <span>555-014-2290</span>
      </div>
      <div class="contact-line">
        <svg viewBox="0 0 10 10" aria-hidden="true"><path d="M0 2h10v6H0z" fill="none" stroke="#fff" stroke-width="1"/><path d="M0 2l5 3.5L10 2" fill="none" stroke="#fff" stroke-width="1"/></svg>
        <span>glen@ambrosk.me</span>
      </div>
    </div>

    <div class="front-web">www.ambrosk.me</div>
  </section>

  <section class="card card-back" aria-label="Business card back">
    <h2 class="back-name">Glen Ambrose</h2>
    <ul class="social-list">
      <li class="social-item"><span class="social-dot"></span>Facepage gambrosk</li>
      <li class="social-item"><span class="social-dot"></span>Chirpline @ambrog</li>
      <li class="social-item"><span class="social-dot"></span>Circlr+ +GlenAmbrose</li>
      <li class="social-item"><span class="social-dot"></span>WorkNexus glenambrose</li>
    </ul>
    <div class="back-web">www.ambrosk.me</div>
  </section>

</main>
</body>
</html>
```